Business Card Design - Carrington Hill Lodge

We are looking at a new design for our business cards that has a modern and professional look. We run a residential aged care facility focussing on the care of residents. The cards will be used for potential clients, consultants and business opportunities in this sector. Blue and white is our main colours and would to see these colours incorporated in the design.
Industry/Entity Type
Business
Contact Information for Business Card
Carrington Hill Lodge, Darren Pelham, dpelham@carringtonhilllodge.com.au, Finance Manager, 0491 736 208, BCom, 48 Yarrabee Way, Wattle Grove, Qld 4173.

```html
<!DOCTYPE html>
<html lang="en">
<head>
<meta charset="utf-8">
<title>Carrington Hill Lodge – Business Card</title>
<link rel="stylesheet" href="https://fonts.googleapis.com/css2?family=Open+Sans:wght@400;600;700&display=swap">
<style>
  :root {
    --brand-blue: #4e7a94;
    --text-blue: #3f6b86;
    --card-white: #ffffff;
    --backdrop: #ecebe8;
  }
  * { box-sizing: border-box; margin: 0; padding: 0; }
  html, body {
    width: 1200px;
    height: 1000px;
    overflow: hidden;
    background: var(--backdrop);
    font-family: "Open Sans", Arial, sans-serif;
  }
  .canvas { position: relative; width: 1200px; height: 1000px; }

  .card {
    position: absolute;
    left: 265px;
    width: 665px;
    height: 397px;
    border-radius: 22px;
    overflow: hidden;
  }
  .card--front { top: 73px; background: var(--card-white); }
  .card--back { top: 533px; background: var(--brand-blue); }

  .band { position: absolute; left: 0; width: 100%; height: 17px; background: var(--brand-blue); }
  .band--top { top: 0; }
  .band--bottom { bottom: 0; }

  .contact { position: absolute; left: 33px; top: 106px; color: var(--text-blue); }
  .contact__name { font-size: 22px; font-weight: 700; letter-spacing: 0.3px; line-height: 1.2; }
  .contact__role { font-size: 18px; font-weight: 400; line-height: 1.3; }

  .divider { position: absolute; left: 0; top: 173px; width: 33px; height: 2px; background: var(--brand-blue); }

  .details { position: absolute; left: 33px; top: 196px; color: var(--text-blue); font-size: 17px; line-height: 1.4; }
  .details__phone { display: flex; align-items: center; gap: 8px; }
  .details__phone svg { width: 14px; height: 14px; fill: var(--text-blue); }
  .details__email { margin-top: 2px; }
  .details__address { margin-top: 10px; }

  .brand {
    position: absolute;
    display: flex;
    flex-direction: column;
    align-items: center;
    gap: 16px;
  }
  .brand--front { left: 345px; top: 130px; width: 300px; color: var(--text-blue); }
  .brand--back { left: 0; top: 130px; width: 100%; color: var(--card-white); }
  .brand__dot { width: 96px; height: 96px; border-radius: 50%; }
  .brand--front .brand__dot { background: var(--brand-blue); }
  .brand--back .brand__dot { background: var(--card-white); }
  .brand__name { font-size: 26px; font-weight: 600; letter-spacing: 0.5px; white-space: nowrap; line-height: 1.2; }
  .brand--back .brand__name { font-size: 30px; }
</style>
</head>
<body>
<main class="canvas">
  <section class="card card--front" aria-label="Business card front">
    <div class="band band--top"></div>
    <div class="contact">
      <p class="contact__name">DARREN PELHAM</p>
      <p class="contact__role">Finance Manager</p>
    </div>
    <div class="divider"></div>
    <div class="details">
      <p class="details__phone">
        <svg viewBox="0 0 24 24" aria-hidden="true"><path d="M6.6 10.8c1.4 2.8 3.8 5.1 6.6 6.6l2.2-2.2c.3-.3.7-.4 1-.2 1.1.4 2.3.6 3.6.6.6 0 1 .4 1 1V20c0 .6-.4 1-1 1C10.6 21 3 13.4 3 4c0-.6.4-1 1-1h3.5c.6 0 1 .4 1 1 0 1.3.2 2.5.6 3.6.1.3 0 .7-.2 1L6.6 10.8z"/></svg>
        0491 736 208
      </p>
      <p class="details__email">dpelham@carringtonhilllodge.com.au</p>
      <p class="details__address">BCom, 48 Yarrabee Way,<br>Wattle Grove, Qld 4173.</p>
    </div>
    <div class="brand brand--front">
      <span class="brand__dot"></span>
      <span class="brand__name">Carrington Hill Lodge</span>
    </div>
    <div class="band band--bottom"></div>
  </section>

  <section class="card card--back" aria-label="Business card back">
    <div class="brand brand--back">
      <span class="brand__dot"></span>
      <span class="brand__name">Carrington Hill Lodge</span>
    </div>
  </section>
</main>
</body>
</html>
```